need a graphic redesign of kelvorahomecare.com

Need a graphic redesign of kelvorahomecare.com. We need to make it more user friendly as well as SEO friendly. All information is there. We have lot of stock photos (done our own photoshoot).

We want this website to be redesigned from scratch. Please avoid using pre made templates. Recommend people who really understand design to approach this project.

Target population is Non resident Indians who live outside India but their families are still in India and need for health care.

Logos and pictures are on the website but we can provide raw images.

Target Market(s)

Industry/Entity Type

Healthcare

Number of Pages Required

5+ page

Font styles to use
Serif
Sans Serif

Requirements
Must have
• Good design, and use of minimal text. Design need to be responsive (we know it is a later process in coding- but mobile devices need to be kept in mind)
Nice to have
• We need a original design.
Should not have
• prebuilt or copied templates

```html
<!DOCTYPE html>
<html lang="en">
<head>
<meta charset="utf-8">
<title>Kelvora Home Care</title>
<link href="https://fonts.googleapis.com/css2?family=Open+Sans:wght@400;600;700&family=Oswald:wght@500;700&display=swap" rel="stylesheet">
<style>
:root{
  --orange:#f39322;
  --orange-soft:#f9c98d;
  --teal:#1d8b9b;
  --ink:#333;
  --muted:#777;
  --light:#f1f1f1;
  --line:#ddd;
  --dark:#262626;
  --darker:#1a1a1a;
  --slate:#2f3a40;
  --white:#fff;
}
*{box-sizing:border-box;margin:0;padding:0}
html,body{width:1200px;height:2792px;overflow:hidden}
body{font-family:"Open Sans",Arial,sans-serif;color:var(--ink);background:var(--white);font-size:12px;line-height:1.5}

.topbar{height:22px;background:#3a3a3a;display:flex;align-items:center;padding:0 170px;color:#ccc;font-size:9px}
.topbar nav{display:flex;height:100%}
.topbar nav a{padding:0 12px;display:flex;align-items:center;color:#ddd;text-decoration:none;text-transform:uppercase;letter-spacing:.5px}
.topbar nav a.active{background:var(--orange);color:#fff}
.topbar .phone{margin-left:auto}

.header{height:70px;display:flex;align-items:center;padding:0 170px}
.brand{display:flex;align-items:center;gap:10px}
.brand-mark{width:30px;height:30px;border-radius:50%;background:var(--orange)}
.brand-name{font-size:20px;font-weight:700;color:var(--teal)}
.member{margin-left:auto;display:flex;align-items:center;gap:10px}
.member span{font-size:15px;color:var(--muted);font-weight:600}
.btn{display:inline-block;font-size:9px;padding:5px 12px;text-transform:uppercase;font-weight:600;text-decoration:none}
.btn-outline{border:1px solid var(--line);color:var(--ink)}
.btn-solid{background:var(--orange);color:#fff}

.hero{position:relative;height:520px;overflow:hidden}
.hero .photo{position:absolute;inset:0;
  background:
    radial-gradient(ellipse 260px 300px at 190px 300px,#f4ede6 0%,rgba(244,237,230,0) 70%),
    radial-gradient(ellipse 200px 260px at 330px 220px,#b8d4dc 0%,rgba(184,212,220,0) 70%),
    radial-gradient(ellipse 220px 300px at 640px 200px,#e9eef1 0%,rgba(233,238,241,0) 70%),
    radial-gradient(ellipse 240px 300px at 900px 230px,#8fb9c7 0%,rgba(143,185,199,0) 70%),
    radial-gradient(ellipse 180px 220px at 1080px 180px,#c9a98d 0%,rgba(201,169,141,0) 70%),
    linear-gradient(90deg,#cfd8dc 0%,#eef2f4 40%,#dfe7ea 60%,#b7c9d1 100%)}
.hero-label{position:absolute;left:0;top:390px;background:var(--orange);color:#fff;font-size:27px;font-weight:600;padding:12px 30px 12px 24px}
.hero-caption{position:absolute;left:552px;top:380px;width:600px;background:var(--teal);color:#fff;padding:8px 16px}
.hero-caption h2{font-family:Georgia,serif;font-size:27px;font-weight:400;line-height:1.3}
.hero-caption p{font-size:10px}
.hero-arrow{position:absolute;top:250px;width:18px;height:26px;background:rgba(0,0,0,.3)}

.features{background:var(--light);padding:50px 170px 0;display:flex;justify-content:space-between;height:360px}
.feature{width:260px;text-align:center}
.feature .icon{width:100px;height:100px;border-radius:50%;background:#9a9a9a;margin:0 auto 18px;display:flex;align-items:center;justify-content:center;color:#fff;font-size:46px;font-weight:700;border:5px solid #ccc}
.feature.highlight .icon{background:var(--orange);border-color:var(--orange-soft)}
.feature h3{font-size:19px;font-weight:700;margin-bottom:8px}
.feature.highlight h3{color:var(--orange)}
.feature p{font-size:10px;color:var(--muted);margin-bottom:18px}
.feature .btn{border:1px solid var(--line);color:var(--ink)}
.feature.highlight .btn{border-color:var(--orange);color:var(--orange)}

.scene{height:360px;position:relative;display:flex;justify-content:center;overflow:hidden}
.scene .art{position:absolute;inset:0;
  background:
    radial-gradient(ellipse 220px 90px at 420px 240px,#f2f2f2 0%,rgba(242,242,242,0) 75%),
    radial-gradient(ellipse 160px 70px at 900px 170px,#c6534b 0%,rgba(198,83,75,0) 75%),
    linear-gradient(180deg,#7f9499 0%,#93a7a6 30%,#9fb49c 48%,#c8c3a4 60%,#6c7174 72%,#4f5356 100%)}
.scene h2{font-family:Oswald,sans-serif;color:#fff;font-size:48px;letter-spacing:1px;margin-top:20px;position:relative;text-shadow:0 2px 6px rgba(0,0,0,.3);line-height:1.2}
.scene h2 small{display:block;font-size:14px;text-align:center;font-weight:500;letter-spacing:3px}

.intro{background:var(--orange);color:#fff;padding:18px 195px 0;font-size:15px;font-weight:600;line-height:1.4;height:80px}
.services{margin:0 195px;background:#fff;border:1px solid var(--line);border-top:none;padding:22px 30px 0;height:330px}
.services .lead{font-size:13px;color:var(--orange);font-weight:600;border-bottom:1px solid var(--line);padding-bottom:12px;margin-bottom:32px}
.services .lead b{color:var(--ink)}
.service-grid{display:grid;grid-template-columns:repeat(3,1fr);gap:48px 30px}
.service{display:flex;gap:14px}
.service svg{flex:none}
.service h4{font-size:15px;color:var(--orange);font-weight:700;line-height:1.2}
.service h5{font-size:10px;color:var(--muted);font-weight:400;margin-bottom:5px}
.service p{font-size:9.5px;color:var(--muted);line-height:1.5}

.team{padding:34px 170px 0;text-align:center;height:350px}
.team h2{font-size:27px;font-weight:400;margin-bottom:6px}
.team .sub{font-size:10px;color:var(--muted);width:560px;margin:0 auto 18px}
.team-row{display:flex;justify-content:space-between}
.member-card{width:128px}
.member-card .photo{height:150px;background:linear-gradient(180deg,#dfe4e8 0%,#b9c3ca 45%,#7e8d97 100%)}
.member-card .name{font-size:9px;color:var(--muted);padding:5px 0;border:1px solid var(--line);border-top:none}

.testimonials{background:var(--slate);color:#fff;height:310px;padding:32px 170px 0;text-align:center;position:relative}
.testimonials h2{font-size:22px;font-weight:400;margin-bottom:24px}
.quote{display:flex;gap:30px;align-items:center;text-align:left;padding-left:40px}
.quote .avatar{width:130px;height:130px;border-radius:50%;background:linear-gradient(180deg,#c9a98d,#8c6a52);border:5px solid #fff;flex:none}
.quote .who{font-size:18px;color:var(--orange);font-weight:600}
.quote .who span{color:#ccc;font-weight:400;font-size:14px}
.quote p{font-size:11px;color:#ccc;margin-top:6px;width:520px}
.dots{position:absolute;bottom:32px;left:0;right:0;display:flex;justify-content:center;gap:6px}
.dots i{width:8px;height:8px;border-radius:50%;background:#777}
.dots i.on{background:var(--orange)}

.partners{height:170px;padding:26px 170px 0}
.partners h3{font-size:11px;font-weight:600;color:var(--muted);text-align:center;margin-bottom:22px}
.badges{display:flex;justify-content:space-between;align-items:center}
.badge{height:64px;background:#e4e4e4;border-radius:4px}

.footer{background:var(--dark);color:#aaa;height:192px;padding:26px 170px 0;display:flex;gap:34px;font-size:9px}
.footer h4{color:#fff;font-size:10px;text-transform:uppercase;margin-bottom:8px;font-weight:700}
.footer h5{color:#ddd;font-size:9px;font-weight:600;margin-bottom:4px}
.footer ul{list-style:none;line-height:1.7}
.footer .col{width:120px}
.footer .contact{display:flex;gap:28px;border-left:1px solid #444;padding-left:20px;height:150px}
.footer .contact div{width:125px}
.footer .follow{margin-left:auto}
.social{display:grid;grid-template-columns:repeat(4,18px);gap:5px}
.social i{width:18px;height:18px;background:#444;display:block}
.copyright{background:var(--darker);color:#888;height:28px;font-size:9px;display:flex;align-items:center;justify-content:center}
</style>
</head>
<body>
<div class="topbar">
  <nav><a class="active" href="#">Home</a><a href="#">About Us</a><a href="#">Services</a><a href="#">Our Plans</a><a href="#">Member Benefits</a><a href="#">Contact</a></nav>
  <span class="phone">Call: +91 11 4000 2200</span>
</div>
<header class="header">
  <div class="brand"><span class="brand-mark"></span><span class="brand-name">Kelvora Home Care</span></div>
  <div class="member"><span>NOT A MEMBER?</span><a class="btn btn-outline" href="#">Login Now</a><a class="btn btn-solid" href="#">Sign Up</a></div>
</header>
<section class="hero">
  <div class="photo" role="img" aria-label="Caregivers and doctors attending to elderly patients at home"></div>
  <span class="hero-arrow" style="left:0"></span><span class="hero-arrow" style="right:0"></span>
  <div class="hero-label">Our Elderly Care Services</div>
  <div class="hero-caption"><h2>touch the lives of millions of NRI's</h2><p>by providing a sustainable support that supports older people who need care back in India</p></div>
</section>
<section class="features">
  <div class="feature"><div class="icon">?</div><h3>WHO WE ARE</h3><p>Caring team of trained doctors and nurses looking after your parents in India with a warm, personal and dependable approach every day.</p><a class="btn" href="#">Read More</a></div>
  <div class="feature highlight"><div class="icon"><svg width="44" height="44" viewBox="0 0 44 44"><path d="M8 23l9 9 19-20" fill="none" stroke="#fff" stroke-width="6"/></svg></div><h3>WHAT WE DO</h3><p>Regular visits, health checks and emergency help for elderly family members so you stay informed while living abroad.</p><a class="btn" href="#">Read More</a></div>
  <div class="feature"><div class="icon">!</div><h3>WHY CHOOSE US</h3><p>Trusted partner hospitals, clear reporting and one point of contact who speaks to you whenever you need an update.</p><a class="btn" href="#">Read More</a></div>
</section>
<section class="scene">
  <div class="art" role="img" aria-label="Illustration of a health care emergency ambulance driving down a city street past a hospital"></div>
  <h2>WE'LL TAKE CARE<small>OF YOUR LOVED ONES</small></h2>
</section>
<section class="intro">Kelvora Home Care is a company providing healthcare services to not only the elderly living in India, but their entire family.</section>
<section class="services">
  <p class="lead">We offer a comprehensive medical assistance program to <b>you and your family which includes the following</b></p>
  <div class="service-grid">
    <div class="service"><svg width="36" height="36" viewBox="0 0 34 34"><circle cx="17" cy="17" r="15" fill="none" stroke="var(--orange)" stroke-width="2"/><path d="M10 17l5 5 9-10" fill="none" stroke="var(--orange)" stroke-width="3"/></svg><div><h4>Regular Check-ups</h4><h5>and Healthcare at Home</h5><p>Scheduled doctor visits and routine tests done at home with reports shared online.</p></div></div>
    <div class="service"><svg width="36" height="36" viewBox="0 0 34 34"><circle cx="17" cy="17" r="15" fill="none" stroke="var(--orange)" stroke-width="2"/><path d="M7 18h6l3-6 3 11 3-5h5" fill="none" stroke="var(--orange)" stroke-width="2"/></svg><div><h4>Monitoring of Vital</h4><h5>Statistics</h5><p>Blood pressure, sugar and heart rate tracked and reviewed by our medical staff.</p></div></div>
    <div class="service"><svg width="36" height="36" viewBox="0 0 34 34"><circle cx="17" cy="17" r="15" fill="none" stroke="var(--orange)" stroke-width="2"/><path d="M9 20h16v-5l-3-4H12l-3 4z" fill="var(--orange)"/><circle cx="12" cy="22" r="2" fill="var(--orange)"/><circle cx="22" cy="22" r="2" fill="var(--orange)"/></svg><div><h4>Transportation</h4><h5>and Escort to Hospitals</h5><p>Safe rides and a trained escort for hospital visits and appointments.</p></div></div>
    <div class="service"><svg width="36" height="36" viewBox="0 0 34 34"><circle cx="17" cy="17" r="15" fill="none" stroke="var(--orange)" stroke-width="2"/><path d="M17 9v16M9 17h16" stroke="var(--orange)" stroke-width="3"/></svg><div><h4>Assured</h4><h5>Services</h5><p>Priority care and quick response from our partner network in every city.</p></div></div>
    <div class="service"><svg width="36" height="36" viewBox="0 0 34 34"><circle cx="17" cy="17" r="15" fill="none" stroke="var(--orange)" stroke-width="2"/><path d="M17 8l8 3v6c0 5-4 8-8 9-4-1-8-4-8-9v-6z" fill="var(--orange)"/></svg><div><h4>Health Insurance</h4><h5>Facilities</h5><p>Guidance on plans, claims and paperwork for the whole family.</p></div></div>
  </div>
</section>
<section class="team">
  <h2>Our Healthcare Team</h2>
  <p class="sub">Experienced doctors and specialists who care for your family as their own, with regular visits and clear advice at every step.</p>
  <div class="team-row">
    <div class="member-card"><div class="photo" role="img" aria-label="Portrait of Dr. Asha Menon"></div><div class="name">Dr. Asha Menon</div></div>
    <div class="member-card"><div class="photo" role="img" aria-label="Portrait of Dr. Ravi Kapoor"></div><div class="name">Dr. Ravi Kapoor</div></div>
    <div class="member-card"><div class="photo" role="img" aria-label="Portrait of Dr. Neha Sethi"></div><div class="name">Dr. Neha Sethi</div></div>
    <div class="member-card"><div class="photo" role="img" aria-label="Portrait of Dr. Arun Das"></div><div class="name">Dr. Arun Das</div></div>
    <div class="member-card"><div class="photo" role="img" aria-label="Portrait of Dr. Meera Joshi"></div><div class="name">Dr. Meera Joshi</div></div>
    <div class="member-card"><div class="photo" role="img" aria-label="Portrait of Dr. Karan Gill"></div><div class="name">Dr. Karan Gill</div></div>
  </div>
</section>
<section class="testimonials">
  <h2>What Our Members Think About Us</h2>
  <div class="quote">
    <div class="avatar" role="img" aria-label="Photo of member Priya Malhotra"></div>
    <div><div class="who">Priya Malhotra <span>- Western Australia</span></div>
    <p>Living so far away, I always worried about my parents. The team visits them regularly, sends me every report and calls me the moment anything changes. I finally feel at peace knowing they are looked after by people who truly care for good.</p></div>
  </div>
  <div class="dots"><i class="on"></i><i></i><i></i></div>
</section>
<section class="partners">
  <h3>Our Partner Hospitals</h3>
  <div class="badges"><span class="badge" style="width:150px"></span><span class="badge" style="width:180px"></span><span class="badge" style="width:160px"></span><span class="badge" style="width:230px"></span></div>
</section>
<footer class="footer">
  <div class="col"><h4>Quick Links</h4><ul><li>Home</li><li>About Us</li><li>Services</li><li>Our Network</li><li>Member Benefits</li><li>Contact</li></ul></div>
  <div class="contact">
    <div><h4>Get In Touch</h4><h5>Registered Office</h5><p>Unit 12, Palm Grove Tower<br>Sector 21, Ring Road<br>New Delhi 110045<br>Ph: +91 11 4000 2200</p></div>
    <div><h4>&nbsp;</h4><h5>Corporate Office</h5><p>4th Floor, Lotus Square<br>MG Road, Phase II<br>Gurugram 122002<br>Ph: +91 124 400 5100</p></div>
    <div><h4>&nbsp;</h4><h5>Our US Office</h5><p>220 Maple Lane<br>Suite 8, Oak Park<br>Edison, NJ 08817<br>Ph: +1 555 0142</p></div>
  </div>
  <div class="follow"><h4>Follow Us On</h4><div class="social"><i></i><i></i><i></i><i></i><i></i><i></i><i></i><i></i></div></div>
</footer>
<div class="copyright">Copyright 2015 kelvorahomecare.com | Site Map | Privacy Policy</div>
</body>
</html>
```